Letter Head Design - Finance industry

Design a letterhead to match the logo. Needs to be clean, simple and crisp. I'm open to suggestions. Will be using the logo that was submitted last with the W crossed over

Target Market(s)

Small medium businesses and government department's

Industry/Entity Type

Industry

Font styles to use
Sans Serif

Colors
cadf82
bcd85c
acd036
9bcb3c
e9e9e9
aaaaaa
000000
7f7f7f
b7b7b7

Requirements
Must have
• Need to display: Logo, Business address, ABN number, ASIC register number, contact phone, website, company email. Details are as per below:

Suite 4B Level 17
Marlowe Harbour Tower
9 Tindall Place
Sydney NSW 2000
Landline Ph: 02 5193 2604
Ph: 1300 4917 63
Email: enquiries@brightmoorfin.com.au
W: www.brightmoorfin.com.au

On the footer, the details below need to be specified:
ABN: 43 719 385 207
ASIC Registration Number: 27 318640571

Should not have
• No imagery or design that is not in line with the logo

```html
<!DOCTYPE html>
<html lang="en">
<head>
<meta charset="utf-8">
<title>Brightmoor Finance Letterhead</title>
<link href="https://fonts.googleapis.com/css2?family=Questrial&display=swap" rel="stylesheet">
<style>
  :root {
    --green-light: #cadf82;
    --green: #9bcb3c;
    --green-mid: #acd036;
    --paper: #ffffff;
    --backdrop: #e9e9e9;
    --rule: #b7b7b7;
    --text-dark: #000000;
    --text-grey: #7f7f7f;
    --text-soft: #aaaaaa;
  }
  * { margin: 0; padding: 0; box-sizing: border-box; }
  html, body { width: 1200px; height: 815px; overflow: hidden; }
  body {
    background: var(--backdrop);
    font-family: "Questrial", "Century Gothic", sans-serif;
    position: relative;
  }
  .letterhead {
    position: absolute;
    top: 70px;
    width: 483px;
    height: 685px;
    background: var(--paper);
  }
  .letterhead--right-aligned { left: 80px; }
  .letterhead--left-aligned { left: 638px; }

  .brand {
    position: absolute;
    top: 40px;
    right: 36px;
    display: flex;
    align-items: center;
    gap: 8px;
  }
  .brand__mark {
    width: 28px;
    height: 28px;
    border-radius: 50%;
    background: var(--green-mid);
  }
  .brand__name {
    font-size: 17px;
    line-height: 17px;
    color: var(--text-grey);
    width: 76px;
  }

  .footer {
    position: absolute;
    bottom: 22px;
    left: 100px;
    right: 36px;
    font-size: 6.6px;
    color: var(--text-dark);
    line-height: 10px;
  }
  .letterhead--left-aligned .footer { left: 36px; right: 100px; text-align: left; }
  .letterhead--right-aligned .footer { text-align: right; }

  .footer__contacts span { margin-left: 6px; white-space: nowrap; }
  .letterhead--left-aligned .footer__contacts span { margin-left: 0; margin-right: 6px; }
  .contact-icon {
    display: inline-block;
    width: 6px;
    height: 6px;
    border-radius: 50%;
    background: var(--green);
    vertical-align: -0.5px;
    margin-right: 2px;
  }
  .footer__rule {
    height: 1px;
    background: var(--rule);
    margin: 3px 0 5px;
  }
  .footer__registration { color: var(--text-grey); }

  .footer-band {
    position: absolute;
    left: 0;
    right: 0;
    bottom: 0;
    height: 12px;
    background: linear-gradient(var(--green-mid), var(--green));
  }
  .letterhead--left-aligned .footer-band { height: 9px; }
</style>
</head>
<body>

<section class="letterhead letterhead--right-aligned">
  <div class="brand">
    <span class="brand__mark"></span>
    <span class="brand__name">Brightmoor Finance</span>
  </div>
  <div class="footer">
    <p class="footer__address">Suite 4B Level 17, Marlowe Harbour Tower, 9 Tindall Place, Sydney NSW 2000</p>
    <p class="footer__contacts">
      <span><i class="contact-icon"></i>+61 2 5193 2604</span>
      <span><i class="contact-icon"></i>1300 4917 63</span>
      <span><i class="contact-icon"></i>enquiries@brightmoorfin.com.au</span>
      <span><i class="contact-icon"></i>www.brightmoorfin.com.au</span>
    </p>
    <div class="footer__rule"></div>
    <p class="footer__registration">ABN: 43 719 385 207 &nbsp;·&nbsp; ASIC Registration Number: 27 318640571</p>
  </div>
  <div class="footer-band"></div>
</section>

<section class="letterhead letterhead--left-aligned">
  <div class="brand">
    <span class="brand__mark"></span>
    <span class="brand__name">Brightmoor Finance</span>
  </div>
  <div class="footer">
    <p class="footer__address">Suite 4B Level 17, Marlowe Harbour Tower, 9 Tindall Place, Sydney NSW 2000</p>
    <p class="footer__contacts">
      <span><i class="contact-icon"></i>+61 2 5193 2604</span>
      <span><i class="contact-icon"></i>1300 4917 63</span>
      <span><i class="contact-icon"></i>enquiries@brightmoorfin.com.au</span>
      <span><i class="contact-icon"></i>www.brightmoorfin.com.au</span>
    </p>
    <div class="footer__rule"></div>
    <p class="footer__registration">ABN: 43 719 385 207 &nbsp;·&nbsp; ASIC Registration Number: 27 318640571</p>
  </div>
  <div class="footer-band"></div>
</section>

</body>
</html>
```